R.T. Marlowe Electrical work flyer

I need a flyer design to help generate some extra work. I'm more than happy for a designer to play around with pictures, text, headings, boarders. The flyer will be double sided A4 size.
We specialize in Residential, Commercial, & Industrial Electrical works including PV Solar System Designs & Installations, Maintenance, System Checks & Upgrades, Mains Upgrades, Overhead & Underground, Switchboard Installations & Upgrades, Safety Switches, Spa & Pool connections, LED Lighting solutions, Energy Audit Checks, Fans & Air Conditioning, Hi-bay Lighting, Carpark Lighting, Data Points, Comms Racks, New Home Builds, Office Fitouts ...
We pride ourselves on always doing a great job, guaranteed workmanship, competitive pricing, & leaving the site clean.
Call Derek for a quote on any of your electrical needs
Mobile:0417 386 204
Email: rtmarloweelectrical@vendamail.example
PO Box 58
Brindle Vale VIC 3194

REC: 38071
CEC Accreditation: A3182096

I've added my company logo & some pics, photo's & electrical / solar brand logos that can be used but not a must. I'm more than happy if you can find better pics.

Target Market(s)

Office, Factory & Home Owners

Industry/Entity Type

Electrical

Font styles to use
Serif
Sans Serif

Requirements
Must have
• eye catchy design with not to much information overload.
• Just aiming for people to call up for quotes etc.
Nice to have
• My company logo, electrical & solar works available
Should not have
• pictures of kids

```html
<!DOCTYPE html>
<html lang="en">
<head>
<meta charset="utf-8">
<title>R.T. Marlowe Electrical — Flyer</title>
<link rel="stylesheet" href="https://fonts.googleapis.com/css2?family=Lato:wght@400;700;900&family=Oswald:wght@500;600&family=Roboto+Condensed:wght@400&display=swap">
<style>
  :root {
    --green: #5fbf35;
    --green-light: #8fd43f;
    --green-deep: #3aa62c;
    --ink: #2a2a2a;
    --charcoal: #333;
    --grey-text: #4a4a4a;
    --blue: #1d6fc4;
    --white: #fff;
    --pill-grey: #dcdcdc;
  }
  * { box-sizing: border-box; margin: 0; padding: 0; }
  html, body { width: 902px; height: 1200px; overflow: hidden; background: #fff; }
  .flyer { position: relative; width: 902px; height: 1200px; overflow: hidden; background: var(--white); font-family: "Lato", sans-serif; }
  .shapes { position: absolute; inset: 0; }

  .brand { position: absolute; left: 50px; top: 66px; display: flex; align-items: center; gap: 14px; }
  .brand-dot { width: 46px; height: 46px; border-radius: 50%; background: var(--green); flex: none; }
  .brand-name { font-family: "Lato", sans-serif; font-weight: 700; font-size: 25px; color: var(--grey-text); line-height: 28px; white-space: nowrap; }

  .pill { position: absolute; height: 44px; display: flex; align-items: center; font-family: "Oswald", sans-serif; font-weight: 600; font-size: 28px; white-space: nowrap; }
  .pill-specialize { left: 0; top: 257px; width: 292px; padding-left: 33px; color: var(--ink); background: linear-gradient(90deg, #fff 0%, #f2f2f2 70%, var(--pill-grey) 100%); border-radius: 0 22px 22px 0; }
  .pill-about { right: 0; top: 621px; width: 190px; padding-left: 30px; color: var(--white); background: var(--ink); border-radius: 22px 0 0 22px; }

  .sectors { position: absolute; left: 28px; top: 319px; list-style: none; }
  .sectors li { font-weight: 700; font-size: 20px; color: var(--ink); line-height: 31.5px; padding-left: 38px; position: relative; white-space: nowrap; }
  .sectors li::before { content: ""; position: absolute; left: 5px; top: 10px; width: 12px; height: 12px; border-radius: 50%; background: var(--white); }
  .sectors .light { font-weight: 400; }

  .services { position: absolute; left: 62px; top: 438px; list-style: none; }
  .services li { font-size: 16.5px; color: var(--ink); line-height: 26.6px; padding-left: 30px; position: relative; white-space: nowrap; }
  .services li::before { content: ""; position: absolute; left: 4px; top: 8px; width: 5px; height: 9px; border: solid var(--white); border-width: 0 2px 2px 0; transform: rotate(40deg); }

  .about { position: absolute; left: 460px; top: 684px; width: 418px; font-size: 13px; line-height: 17px; color: var(--ink); text-align: justify; }
  .about p + p { margin-top: 9px; }

  .call { position: absolute; right: 24px; top: 894px; font-family: "Roboto Condensed", sans-serif; font-size: 15.5px; color: var(--green-deep); white-space: nowrap; }
  .phone { position: absolute; left: 644px; top: 925px; font-family: "Oswald", sans-serif; font-weight: 600; font-size: 38px; color: var(--ink); line-height: 1; white-space: nowrap; }
  .phone svg { position: absolute; left: -46px; top: 8px; }

  .accreditation { position: absolute; left: 436px; top: 1080px; color: var(--white); font-family: "Roboto Condensed", sans-serif; font-size: 12.5px; line-height: 28px; white-space: nowrap; }
  .divider { position: absolute; left: 600px; top: 1074px; width: 2px; height: 60px; background: var(--white); }
  .contact { position: absolute; left: 614px; top: 1074px; color: var(--white); font-weight: 700; font-size: 12px; list-style: none; white-space: nowrap; }
  .contact li { position: relative; padding-left: 22px; line-height: 17px; }
  .contact li + li { margin-top: 14px; }
  .contact svg { position: absolute; left: 0; top: 3px; }
</style>
</head>
<body>
<main class="flyer">
  <svg class="shapes" width="902" height="1200" viewBox="0 0 902 1200">
    <defs>
      <linearGradient id="greenFade" x1="0" y1="0" x2="1" y2="0">
        <stop offset="0" stop-color="#4fb532"/>
        <stop offset="1" stop-color="#93d63f"/>
      </linearGradient>
      <linearGradient id="skyTone" x1="0" y1="0" x2="0.4" y2="1">
        <stop offset="0" stop-color="#3f86d6"/>
        <stop offset="0.55" stop-color="#8fb8e6"/>
        <stop offset="1" stop-color="#3d5fa8"/>
      </linearGradient>
      <linearGradient id="poolTone" x1="0" y1="0" x2="0" y2="1">
        <stop offset="0" stop-color="#8fb2d8"/>
        <stop offset="0.45" stop-color="#6e9a5a"/>
        <stop offset="0.7" stop-color="#47a9de"/>
        <stop offset="1" stop-color="#1d80c9"/>
      </linearGradient>
      <linearGradient id="techTone" x1="0" y1="0" x2="1" y2="1">
        <stop offset="0" stop-color="#c9ccd2"/>
        <stop offset="1" stop-color="#36405a"/>
      </linearGradient>
      <linearGradient id="darkPanel" x1="0" y1="0" x2="0" y2="1">
        <stop offset="0" stop-color="#4a4a4a"/>
        <stop offset="1" stop-color="#262626"/>
      </linearGradient>
    </defs>

    <path d="M0,175 C140,210 300,200 470,140 L470,178 C320,230 150,240 0,210 Z" fill="var(--ink)"/>
    <path d="M0,205 C150,236 320,222 470,165 L470,360 C462,540 440,720 432,905 L0,905 Z" fill="url(#greenFade)"/>
    <path d="M470,360 C462,540 440,720 432,905 L448,905 C456,720 476,540 484,360 Z" fill="#d8d8d8"/>

    <ellipse cx="812" cy="146" rx="452" ry="430" fill="var(--ink)"/>
    <ellipse cx="818" cy="146" rx="442" ry="420" fill="var(--white)"/>
    <ellipse cx="820" cy="148" rx="436" ry="414" fill="var(--green)"/>
    <ellipse cx="823" cy="150" rx="420" ry="398" fill="url(#skyTone)" role="img" aria-label="Photo: two electricians installing solar panels on a roof under a blue sky"/>

    <path d="M0,890 C130,868 300,885 440,935 L440,1200 L0,1200 Z" fill="var(--ink)"/>
    <path d="M0,905 C130,884 300,898 432,948 L432,1200 L0,1200 Z" fill="url(#poolTone)" role="img" aria-label="Photo: backyard swimming pool and spa beside a lawn with palm trees"/>

    <path d="M432,978 C600,992 780,1010 902,1034" fill="none" stroke="#cfcfcf" stroke-width="6"/>
    <path d="M432,990 C600,1004 780,1022 902,1046" fill="none" stroke="var(--blue)" stroke-width="7"/>
    <path d="M432,1004 C600,1016 780,1034 902,1060 L902,1200 L432,1200 Z" fill="url(#darkPanel)"/>

    <ellipse cx="462" cy="980" rx="94" ry="90" fill="var(--ink)"/>
    <ellipse cx="462" cy="980" rx="86" ry="82" fill="url(#techTone)" role="img" aria-label="Photo: electrician in uniform checking a clipboard"/>
  </svg>

  <div class="brand">
    <span class="brand-dot"></span>
    <span class="brand-name">R.T. Marlowe<br>Electrical</span>
  </div>

  <h2 class="pill pill-specialize">We Specialize In</h2>

  <ul class="sectors">
    <li>Residential</li>
    <li>Commercial</li>
    <li>Industrial Electrical works <span class="light">including</span></li>
  </ul>

  <ul class="services">
    <li>PV Solar System Designs &amp; Installations</li>
    <li>Maintenance</li>
    <li>System Checks &amp; Upgrades</li>
    <li>Mains Upgrades</li>
    <li>Overhead &amp; Underground</li>
    <li>Switchboard Installations &amp; Upgrades</li>
    <li>Safety Switches</li>
    <li>Spa &amp; Pool connections</li>
    <li>LED Lighting solutions</li>
    <li>Energy Audit Checks</li>
    <li>Fans &amp; Air Conditioning</li>
    <li>Hi-bay Lighting</li>
    <li>Carpark Lighting</li>
    <li>Data Points</li>
    <li>Comms Racks</li>
    <li>New Home Builds, Office Fitouts ...</li>
  </ul>

  <h2 class="pill pill-about">About Us</h2>

  <div class="about">
    <p>Lorem ipsum dolor sit amet, consectetuer adipiscing elit. Aenean commodo ligula eget dolor. Aenean massa. Cum sociis natoque penatibus et magnis dis parturient montes, nascetur ridiculus mus. Donec quam felis, ultricies nec, pellentesque eu, pretium quis, sem. Nulla consequat massa quis enim. Donec pede justo, fringilla vel, aliquet nec, vulputate eget, arcu.</p>
    <p>In enim justo, rhoncus ut, imperdiet a, venenatis vitae, justo. Nullam dictum felis eu pede mollis pretium. Integer tincidunt. Cras dapibus. Vivamus elementum semper nisi. Aenean vulputate eleifend tellus.</p>
  </div>

  <p class="call">Call Derek for a quote on any of your electrical needs</p>
  <p class="phone">
    <svg width="28" height="28" viewBox="0 0 28 28" aria-hidden="true">
      <path d="M6,4 L10,4 L12,10 L9,12 C10.5,15.5 12.5,17.5 16,19 L18,16 L24,18 L24,22 C24,24 22,25 20,25 C11,24 4,17 3,8 C3,6 4,4 6,4 Z" fill="var(--green-deep)"/>
      <path d="M16,3 A9,9 0 0 1 25,12" fill="none" stroke="var(--green-deep)" stroke-width="2"/>
      <path d="M16,8 A4,4 0 0 1 20,12" fill="none" stroke="var(--green-deep)" stroke-width="2"/>
    </svg>0417 386 204</p>

  <div class="accreditation">
    <p>REC: 38071</p>
    <p>CEC Accreditation: A3182096</p>
  </div>
  <span class="divider"></span>
  <ul class="contact">
    <li>
      <svg width="14" height="11" viewBox="0 0 14 11" aria-hidden="true"><rect x="0" y="0" width="14" height="11" fill="var(--white)"/><path d="M0,0 L7,6 L14,0" fill="none" stroke="var(--charcoal)" stroke-width="1.4"/></svg>
      rtmarloweelectrical@vendamail.example
    </li>
    <li>
      <svg width="14" height="13" viewBox="0 0 14 13" aria-hidden="true"><path d="M7,0 L14,6 L12,6 L12,13 L8.5,13 L8.5,9 L5.5,9 L5.5,13 L2,13 L2,6 L0,6 Z" fill="var(--white)"/></svg>
      PO Box 58<br>Brindle Vale VIC 3194
    </li>
  </ul>
</main>
</body>
</html>
```